Business card for law firm

Need business card for new law firm. Think confident, authoritative, conservative, but not stuffy or old-fashioned.

Contact Information for Business Card

Content for card - logo (uploaded), plus the following:

Paul Wexbury (larger font)
Managing Partner (larger font, but not as large as name)
Level 9, 41 Tansy Lane
Sydney NSW 2000
Main Tel 02 7346 2190
Direct Tel 02 6273 4415
Email paul@qvlegal.com.au
www.qvlegal.com.au

Letterhead design should include logo plus:
Level 9, 41 Tansy Lane
Sydney NSW 2000
Tel 02 6273 4415
www.qvlegal.com.au

```html
<!DOCTYPE html>
<html lang="en">
<head>
<meta charset="UTF-8">
<title>Quillvane Lawyers – Business Card</title>
<link href="https://fonts.googleapis.com/css2?family=Mulish:wght@600;700&family=Arimo:wght@400&display=swap" rel="stylesheet">
<style>
  :root {
    --stage: #2a2a2c;
    --card-white: #ffffff;
    --card-dark: #1f1f20;
    --navy: #1c2260;
    --brand-blue: #1e5aa0;
    --ink-grey: #4a4a4a;
    --emboss: #141415;
  }
  * { margin: 0; padding: 0; box-sizing: border-box; }
  html, body { width: 1200px; height: 900px; overflow: hidden; }
  body {
    background: var(--stage);
    display: flex;
    align-items: center;
    justify-content: center;
    gap: 60px;
    font-family: "Arimo", Arial, sans-serif;
  }
  .card {
    width: 500px;
    height: 300px;
    position: relative;
    box-shadow: 0 18px 40px rgba(0,0,0,0.45);
  }
  .card--front { background: var(--card-white); padding: 40px 40px; }
  .card--back {
    background: var(--card-dark);
    display: flex; align-items: center; justify-content: center;
  }
  .holder-name {
    font-family: "Mulish", sans-serif;
    font-weight: 700;
    font-size: 26px;
    color: var(--brand-blue);
    line-height: 1.1;
  }
  .holder-title {
    font-size: 17px;
    color: var(--ink-grey);
    margin-top: 2px;
  }
  .address {
    margin-top: 30px;
    font-size: 14px;
    color: var(--ink-grey);
    line-height: 1.35;
    padding-left: 24px;
  }
  .contact-list { list-style: none; margin-top: 4px; font-size: 14px; color: var(--ink-grey); }
  .contact-list li { display: flex; align-items: center; line-height: 1.35; }
  .contact-icon {
    width: 24px; flex: 0 0 24px;
    display: flex; align-items: center;
    color: var(--brand-blue);
    font-family: "Mulish", sans-serif; font-weight: 700; font-size: 15px;
  }
  .contact-icon svg { width: 15px; height: 15px; }
  .brand {
    display: flex; align-items: center; gap: 10px;
    font-family: "Mulish", sans-serif;
    font-weight: 600;
    letter-spacing: 0.06em;
    text-transform: uppercase;
  }
  .brand-mark { display: block; }
  .card--front .brand {
    position: absolute; right: 40px; bottom: 36px;
    font-size: 19px; color: var(--navy);
  }
  .card--front .brand-mark { width: 18px; height: 18px; background: var(--navy); }
  .card--back .brand { font-size: 30px; color: var(--emboss); }
  .card--back .brand-mark { width: 26px; height: 26px; background: var(--navy); }
</style>
</head>
<body>
  <section class="card card--front" aria-label="Card front">
    <h1 class="holder-name">Paul Wexbury</h1>
    <p class="holder-title">Managing Partner</p>
    <p class="address">Level 9, 41 Tansy Lane<br>Sydney NSW 2000</p>
    <ul class="contact-list">
      <li>
        <span class="contact-icon">
          <svg viewBox="0 0 24 24" aria-hidden="true"><path fill="currentColor" d="M6.6 10.8a15.1 15.1 0 0 0 6.6 6.6l2.2-2.2a1 1 0 0 1 1-.25 11.4 11.4 0 0 0 3.6.57 1 1 0 0 1 1 1V20a1 1 0 0 1-1 1A17 17 0 0 1 3 4a1 1 0 0 1 1-1h3.5a1 1 0 0 1 1 1c0 1.25.2 2.45.57 3.6a1 1 0 0 1-.25 1z"/></svg>
        </span>02 6273 4415
      </li>
      <li><span class="contact-icon"></span>02 7346 2190</li>
      <li><span class="contact-icon">@</span>paul@qvlegal.com.au</li>
      <li>
        <span class="contact-icon">
          <svg viewBox="0 0 24 24" aria-hidden="true" fill="none" stroke="currentColor" stroke-width="1.6"><circle cx="12" cy="12" r="9.5"/><ellipse cx="12" cy="12" rx="4.5" ry="9.5"/><path d="M2.5 12h19M4 7h16M4 17h16"/></svg>
        </span>www.qvlegal.com.au
      </li>
    </ul>
    <div class="brand"><span class="brand-mark"></span>Quillvane Lawyers</div>
  </section>

  <section class="card card--back" aria-label="Card back">
    <div class="brand"><span class="brand-mark"></span>Quillvane Lawyers</div>
  </section>
</body>
</html>
```